Complete Restaurant Branding Project

Bistro Velluto is looking for new ideas and designs for our various branded items.

You will be required to design the following items:

1) Staff Uniforms
2) Dine In Menu
3) Take Out Menu
4) Food Take Out Packaging
5) Take Out Bags
6) Beverage Take Out Cups
7) Dine in plates, coffee cups, mugs, etc...
8) Feel free to design any other brandable items related to our business

Please check our website to get a feel of our restaurant. Make sure to check the menu and the different dishes we offer to help you in the food packaging design and menu design. http://www.bistrovelluto-example.com/

We are open to new ideas, so we intentionally won't specify details such as materials, sizes, or shapes for any item.

We refined our logo in a contest a few days ago, the new logo is attached. Please don't use the logo from the website or any graphic elements from the website theme in your designs.

```html
<!DOCTYPE html>
<html lang="en">
<head>
<meta charset="utf-8">
<title>Bistro Velluto – Dine-in Menu Covers</title>
<link rel="stylesheet" href="https://fonts.googleapis.com/css2?family=Playball&family=Roboto:wght@400;500&display=swap">
<style>
  :root {
    --board: #e6e6e6;
    --label: #a9a9a9;
    --caption: #7a7a7a;
    --cover-brown: #5a3621;
    --cover-brown-light: #6e4328;
    --cover-brown-dark: #4c2c1a;
    --band-gold: #d5ad3f;
    --band-gold-light: #e2bd4e;
    --band-gold-dark: #c69f35;
    --seal-brown: #7a3a1c;
    --seal-gold: #f1cb5c;
    --menu-ink: #4a2614;
    --url-ink: #ffffff;
  }
  html, body {
    margin: 0;
    padding: 0;
    overflow: hidden;
  }
  .board {
    position: relative;
    width: 1200px;
    height: 795px;
    background: var(--board);
    font-family: "Roboto", Arial, sans-serif;
    overflow: hidden;
  }
  .side-label {
    position: absolute;
    top: 66px;
    font-size: 13px;
    color: var(--label);
    margin: 0;
  }
  .side-label--back { left: 145px; }
  .side-label--front { left: 1018px; }
  .cover {
    position: absolute;
    top: 99px;
    height: 600px;
    box-shadow: 2px 3px 6px rgba(0,0,0,0.25);
    overflow: hidden;
  }
  .cover--back { left: 146px; width: 455px; }
  .cover--front { left: 624px; width: 430px; }
  .cover__pattern {
    position: absolute;
    inset: 0;
    background:
      radial-gradient(ellipse at 30% 25%, var(--cover-brown-light) 0%, transparent 60%),
      radial-gradient(ellipse at 70% 80%, var(--cover-brown-light) 0%, transparent 55%),
      linear-gradient(160deg, var(--cover-brown) 0%, var(--cover-brown-dark) 100%);
  }
  .cover__url {
    position: absolute;
    top: 293px;
    left: 0;
    width: 100%;
    text-align: center;
    color: var(--url-ink);
    font-size: 13px;
    margin: 0;
  }
  .cover__band {
    position: absolute;
    top: 0;
    left: 114px;
    width: 195px;
    height: 100%;
    background:
      radial-gradient(ellipse at 50% 15%, var(--band-gold-light) 0%, transparent 60%),
      radial-gradient(ellipse at 50% 75%, var(--band-gold-light) 0%, transparent 55%),
      linear-gradient(180deg, var(--band-gold) 0%, var(--band-gold-dark) 100%);
  }
  .brand-seal {
    position: absolute;
    top: 131px;
    left: 113px;
    width: 198px;
    height: 198px;
    border-radius: 50%;
    background: var(--seal-brown);
    display: flex;
    align-items: center;
    justify-content: center;
  }
  .brand-seal__name {
    font-family: "Playball", cursive;
    font-size: 32px;
    color: var(--seal-gold);
    margin: 0;
    text-align: center;
    line-height: 1.1;
  }
  .cover__title {
    position: absolute;
    top: 448px;
    left: 114px;
    width: 195px;
    text-align: center;
    font-family: "Playball", cursive;
    font-weight: 400;
    font-size: 58px;
    color: var(--menu-ink);
    margin: 0;
  }
  .board__caption {
    position: absolute;
    right: 20px;
    top: 748px;
    font-size: 24px;
    font-weight: 500;
    color: var(--caption);
    margin: 0;
  }
</style>
</head>
<body>
  <main class="board">
    <p class="side-label side-label--back">Back</p>
    <p class="side-label side-label--front">Front</p>

    <section class="cover cover--back">
      <div class="cover__pattern" role="img" aria-label="Brown floral damask pattern covering the back cover"></div>
      <p class="cover__url">www.BistroVelluto-example.com</p>
    </section>

    <section class="cover cover--front">
      <div class="cover__pattern" role="img" aria-label="Brown floral damask pattern covering the front cover"></div>
      <div class="cover__band" role="img" aria-label="Vertical gold band with tonal floral pattern"></div>
      <div class="brand-seal">
        <p class="brand-seal__name">Bistro<br>Velluto</p>
      </div>
      <h1 class="cover__title">Menu</h1>
    </section>

    <p class="board__caption">Dine-in Menu</p>
  </main>
</body>
</html>
```